Actors Postcard Design

I need a postcard designed for me. I am an actor, voice over artist and technical adviser for tv, film and videogames. I am open to color ideas. My photos are in black and white so something to make those stand out a bit. Masculine colors like dark blue etc..I have seen some of your designs with 3 photos which I liked. Perhaps a 2-3 photo scheme. Back of postcard to contain my resume. Want it to look professional and not cartoonish (since I mentioned video games). Front to have photos and job title and contact info

Please take my color direction lightly, I am open to all color schemes. light or dark. You are the professionals. Am looking forward to seeing what all of you come up with. Thanks

Tv

```html
<!DOCTYPE html>
<html lang="en">
<head>
<meta charset="utf-8">
<title>Actor Postcard – Back</title>
<link rel="stylesheet" href="https://fonts.googleapis.com/css2?family=Roboto+Condensed:wght@400;700&family=Roboto:wght@400&display=swap">
<style>
  :root {
    --teal: #14b1c2;
    --panel: #ccffff;
    --ink: #1a33cc;
    --orange: #ffbb00;
    --green: #66ff00;
    --aqua: #44dddd;
    --purple: #9944ff;
    --stamp: #88c4dd;
    --rule: #9ccbe8;
    --white: #ffffff;
  }
  html, body { margin: 0; padding: 0; overflow: hidden; background: var(--white); }
  .postcard {
    position: relative; width: 1200px; height: 923px; overflow: hidden;
    background: var(--white);
    font-family: "Roboto Condensed", "Arial Narrow", sans-serif;
  }
  .backdrop { position: absolute; left: 0; top: 0; }
  .actor-name {
    position: absolute; left: 32px; top: 30px; margin: 0; white-space: nowrap;
    color: var(--white); font-weight: 700; font-size: 38px; letter-spacing: 0.2px;
  }
  .section-title {
    position: absolute; left: 35px; top: 94px; margin: 0;
    color: var(--ink); font-weight: 700; font-size: 34px;
  }
  .contact {
    position: absolute; left: 533px; top: 46px; width: 334px;
    color: var(--white); text-align: center;
  }
  .contact .phone { font-family: "Roboto", Arial, sans-serif; font-size: 33px; line-height: 40px; }
  .contact .email { font-family: "Roboto", Arial, sans-serif; font-size: 24px; line-height: 32px; }
  .contact .divider { height: 2px; background: var(--white); margin: 14px 0 12px; }
  .stats {
    display: grid; grid-template-columns: 165px 150px;
    padding-left: 20px; text-align: left; font-size: 29px; line-height: 35px;
  }
  .label {
    position: absolute; left: 0; width: 230px; height: 34px; padding-left: 33px;
    color: var(--white); font-size: 28px; line-height: 34px;
  }
  .label--acting { top: 145px; background: var(--orange); }
  .label--voice { top: 290px; background: var(--green); }
  .label--tech { top: 438px; background: var(--aqua); }
  .label--skills { top: 609px; background: var(--purple); }
  .entries {
    position: absolute; left: 33px; margin: 0; padding: 0; list-style: none;
    color: var(--ink); font-size: 20px; line-height: 30px; white-space: nowrap;
  }
  .entries li.sub { padding-left: 17px; }
  .entries li.sub2 { padding-left: 27px; }
  .entries--acting { top: 183px; }
  .entries--voice { top: 327px; line-height: 31.5px; }
  .entries--tech { top: 475px; line-height: 27px; }
  .entries--tech li + li { margin-top: 7px; }
  .entries--skills { top: 648px; line-height: 27.5px; }
  .postage {
    position: absolute; left: 975px; top: 75px; width: 140px; height: 140px;
    border: 2px solid var(--stamp); color: var(--stamp);
    font-family: "Roboto", Arial, sans-serif; font-size: 23px; line-height: 31px;
    text-align: center; box-sizing: border-box; padding-top: 36px;
  }
  .address-line {
    position: absolute; left: 695px; width: 406px; height: 2px; background: var(--rule);
  }
</style>
</head>
<body>
<div class="postcard">
  <svg class="backdrop" width="1200" height="923" viewBox="0 0 1200 923" aria-hidden="true">
    <rect x="0" y="0" width="578" height="768" fill="var(--panel)"/>
    <polygon points="0,0 900,0 900,215 578,270 388,85 0,85" fill="var(--teal)"/>
    <rect x="900" y="0" width="5" height="217" fill="var(--orange)"/>
    <rect x="0" y="763" width="140" height="5" fill="var(--green)"/>
    <rect x="140" y="763" width="438" height="5" fill="var(--orange)"/>
  </svg>

  <h1 class="actor-name">TOMASZ “TOM” BARANSKI</h1>
  <h2 class="section-title">Training/Experience</h2>

  <div class="contact">
    <div class="phone">555-014-2286</div>
    <div class="email">tomaszbaranski@mailbox.net</div>
    <div class="divider"></div>
    <div class="stats">
      <span>Height: 5’11”</span><span>Hair: Brown</span>
      <span>Weight: 175</span><span>Eyes: Hazel</span>
    </div>
  </div>

  <div class="label label--acting">Acting</div>
  <ul class="entries entries--acting">
    <li>Harbor Lane Acting School - 2 yrs</li>
    <li>Stagecraft Studio Academy – On Camera 3yrs</li>
    <li>NCS Acting Coach Northland – 4 day intensive</li>
  </ul>

  <div class="label label--voice">Voice Over</div>
  <ul class="entries entries--voice">
    <li>Voice Forge - Studio Workshop (commercial, narration etc..)</li>
    <li class="sub">- Adv Studio Workshop</li>
    <li class="sub2">- 3 day Animation Intensive</li>
  </ul>

  <div class="label label--tech">Technical Advising</div>
  <ul class="entries entries--tech">
    <li>FNB Special Agent – 12 yrs</li>
    <li>Extensive Firearms Training – FNB, Northline Tactics, Former Ranger<br>Members, Army SRT. Defensive Tactics, Entry Work, Vehicle<br>Containment, Surveillance, etc…</li>
  </ul>

  <div class="label label--skills">Special Skills</div>
  <ul class="entries entries--skills">
    <li>12 yrs martial arts (Karate, Boxing, Aikido, Escrima), EMT,<br>Personal Trainer, Sailing, Skiing, Rock Climbing, Whitewater<br>Kayaking, Fencing, Trail Running, Surfing, Woodturning,<br>Welding 5yrs. Fluent Czech.</li>
  </ul>

  <div class="postage">Postage<br>Area</div>
  <div class="address-line" style="top:440px"></div>
  <div class="address-line" style="top:512px"></div>
  <div class="address-line" style="top:582px"></div>
  <div class="address-line" style="top:653px"></div>
</div>
</body>
</html>
```